Modern business card and stationary design for Tech consulting company (startup)
Veromb Technologies Limited
Modern business card and stationary design for Tech consulting company (startup) - Information Technology
Creative Brief
Professional
Malcolm Dewhurst
CEO
Suite 24613 Lower Ground Floor 212-224 Harwell Road London, N7 2QD
mdewhurst@veromb.co.uk
www.veromb.co.uk
Designers, This project is for business card and stationary design. What I’m looking for is design based around the colour scheme of the attached logo. As yet the website is still being designed, but the attached business logo will give you a reference point for the corporate colours. I have attached a couple of links with a general idea of what I’m looking for; http://www.plandoria.com/drafts/display/contest/518230/draft/3047612 http://www.plandoria.com/drafts/display/contest/518230/draft/3048945 All submitted designs will be rated on a regular basis. If you have any further questions relating to this project, please let get in touch. The winning design will be required to provide editable versions of the files (i.e. personal contact details etc.) Good luck

```html
<!DOCTYPE html>
<html lang="en">
<head>
<meta charset="utf-8">
<title>Veromb Technologies — Stationery Concepts</title>
<link href="https://fonts.googleapis.com/css2?family=Montserrat:wght@400;600;700&display=swap" rel="stylesheet">
<style>
  :root {
    --backdrop: #ece9e4;
    --paper: #ffffff;
    --red: #c8202a;
    --red-dark: #9e1219;
    --grey: #a9a9a9;
    --grey-light: #d9d9d9;
    --ink: #3a3a3a;
    --label: #4a4a4a;
    --faint: #f1f1f1;
  }
  * { margin: 0; padding: 0; box-sizing: border-box; }
  html, body { width: 1200px; height: 626px; overflow: hidden; }
  body {
    position: relative;
    background: var(--backdrop);
    font-family: "Montserrat", sans-serif;
    color: var(--ink);
  }
  .sheet {
    position: absolute;
    background: var(--paper);
    overflow: hidden;
    box-shadow: 0 2px 6px rgba(0,0,0,.18);
  }
  .sheet svg.wave { position: absolute; display: block; }
  .label {
    position: absolute;
    font-size: 9px;
    letter-spacing: 1.6px;
    text-transform: uppercase;
    color: var(--label);
  }
  .brand {
    position: absolute;
    display: flex;
    align-items: center;
    gap: 6px;
  }
  .brand-mark { background: var(--red); flex: none; }
  .brand-name {
    font-weight: 700;
    color: var(--red);
    line-height: 1;
    text-transform: uppercase;
    letter-spacing: .5px;
  }

  /* Business cards */
  .card { left: 24px; width: 164px; height: 102px; }
  .card-front { top: 222px; }
  .card-back { top: 353px; }
  .card-front .brand { left: 12px; top: 10px; }
  .card-front .brand-mark { width: 9px; height: 9px; }
  .card-front .brand-name { font-size: 9px; }
  .card-contact {
    position: absolute; left: 12px; top: 30px;
    font-size: 4.2px; line-height: 6.4px; color: var(--ink);
  }
  .card-contact .person { font-weight: 700; font-size: 5px; }
  .card-back .brand { left: 14px; top: 38px; }
  .card-back .brand-mark { width: 11px; height: 11px; }
  .card-back .brand-name { font-size: 10px; }

  /* Letterhead */
  .letterhead { left: 257px; top: 29px; width: 341px; height: 494px; }
  .letterhead .brand { left: 44px; top: 26px; }
  .letterhead .brand-mark { width: 13px; height: 13px; }
  .letterhead .brand-name { font-size: 12px; }
  .letterhead-watermark {
    position: absolute; left: 120px; top: 200px;
    width: 100px; height: 100px; background: var(--faint);
  }
  .letterhead-contact {
    position: absolute; left: 168px; top: 418px;
    font-size: 4.4px; line-height: 7px; color: #fff;
  }

  /* Envelopes */
  .envelope { left: 691px; width: 470px; }
  .envelope-back { top: 115px; height: 209px; }
  .envelope-back .brand { left: 225px; top: 22px; }
  .envelope-back .brand-mark { width: 20px; height: 20px; }
  .envelope-front { top: 365px; height: 206px; }
  .envelope-front .brand { left: 16px; top: 18px; }
  .envelope-front .brand-mark { width: 16px; height: 16px; }
  .envelope-front .brand-name { font-size: 14px; }
</style>
</head>
<body>

  <p class="label" style="left:40px; top:164px;">Stationery Concepts</p>

  <!-- Business card front -->
  <section class="sheet card card-front" aria-label="Business card front">
    <div class="brand"><span class="brand-mark"></span><span class="brand-name">Veromb Technologies</span></div>
    <div class="card-contact">
      <div class="person">Malcolm Dewhurst</div>
      <div>CEO</div>
      <div>Suite 24613 Lower Ground Floor</div>
      <div>212-224 Harwell Road London, N7 2QD</div>
      <div>+44 (0)20 7946 0815</div>
      <div>mdewhurst@veromb.co.uk</div>
      <div>www.veromb.co.uk</div>
    </div>
    <svg class="wave" style="left:0; bottom:0;" width="164" height="34" viewBox="0 0 164 34" preserveAspectRatio="none">
      <path d="M0,22 C50,4 110,2 164,8 L164,14 C110,8 50,12 0,28 Z" fill="var(--grey)"/>
      <path d="M0,28 C50,12 110,10 164,14 L164,34 L0,34 Z" fill="var(--red)"/>
    </svg>
  </section>
  <p class="label" style="left:40px; top:333px;">Business Card Front</p>

  <!-- Business card back -->
  <section class="sheet card card-back" aria-label="Business card back">
    <div class="brand"><span class="brand-mark"></span><span class="brand-name">Veromb Technologies</span></div>
    <svg class="wave" style="left:0; bottom:0;" width="164" height="22" viewBox="0 0 164 22" preserveAspectRatio="none">
      <path d="M0,8 C40,10 80,14 164,20 L164,22 L0,22 Z" fill="var(--red)"/>
    </svg>
  </section>
  <p class="label" style="left:40px; top:464px;">Business Card Back</p>

  <!-- Letterhead -->
  <section class="sheet letterhead" aria-label="Letterhead">
    <svg class="wave" style="left:0; top:0;" width="200" height="90" viewBox="0 0 200 90" preserveAspectRatio="none">
      <path d="M0,0 L200,0 C120,4 50,22 0,90 Z" fill="var(--grey-light)"/>
      <path d="M0,0 L170,0 C100,4 36,20 0,78 Z" fill="var(--red)"/>
    </svg>
    <div class="brand"><span class="brand-mark"></span><span class="brand-name">Veromb Technologies</span></div>
    <div class="letterhead-watermark"></div>
    <svg class="wave" style="left:0; bottom:0;" width="341" height="110" viewBox="0 0 341 110" preserveAspectRatio="none">
      <path d="M0,62 C90,30 200,10 341,14 L341,26 C200,24 100,40 0,72 Z" fill="var(--grey)"/>
      <path d="M0,72 C100,40 200,26 341,26 L341,110 L0,110 Z" fill="var(--red)"/>
      <path d="M0,96 C110,74 220,66 341,70 L341,110 L0,110 Z" fill="var(--red-dark)" opacity=".45"/>
    </svg>
    <div class="letterhead-contact">
      <div>Suite 24613 Lower Ground Floor, 212-224 Harwell Road</div>
      <div>London, N7 2QD</div>
      <div>+44 (0)20 7946 0815</div>
      <div>mdewhurst@veromb.co.uk</div>
      <div>www.veromb.co.uk</div>
    </div>
  </section>
  <p class="label" style="left:355px; top:584px;">Letter Head Option 1</p>

  <!-- Envelope back -->
  <section class="sheet envelope envelope-back" aria-label="Envelope back">
    <svg class="wave" style="left:0; top:0;" width="470" height="209" viewBox="0 0 470 209" preserveAspectRatio="none">
      <path d="M0,0 L235,118 L470,0" fill="none" stroke="var(--grey-light)" stroke-width="1.5"/>
      <path d="M0,209 L200,110 M470,209 L270,110" fill="none" stroke="var(--grey-light)" stroke-width="1"/>
    </svg>
    <div class="brand"><span class="brand-mark"></span></div>
  </section>

  <!-- Envelope front -->
  <section class="sheet envelope envelope-front" aria-label="Envelope front">
    <div class="brand"><span class="brand-mark"></span><span class="brand-name">Veromb Technologies</span></div>
    <svg class="wave" style="left:0; bottom:0;" width="470" height="70" viewBox="0 0 470 70" preserveAspectRatio="none">
      <path d="M0,40 C140,14 300,4 470,6 L470,16 C300,16 150,28 0,50 Z" fill="var(--grey)"/>
      <path d="M0,50 C150,28 300,16 470,16 L470,70 L0,70 Z" fill="var(--red)"/>
      <path d="M0,62 C160,46 320,40 470,44 L470,70 L0,70 Z" fill="var(--red-dark)" opacity=".45"/>
    </svg>
  </section>
  <p class="label" style="left:866px; top:584px;">Envelope Option 3</p>

</body>
</html>
```